A5 2 sided flyer to promote pharmacy services

We need a leaflet design which promotes our pharmacy and its services. We are a modern, chic hip, funky new pharmacy, and our leaflet should reflect this.
We are looking for an exciting design fun design with limited pictures of people on it.
It needs to be 2 sided, the first side to include name, address, telephone number, twitter and facebook handle, opening hours. I want to highlight our main service with is prescription collection, I like the idea of having a cartoon type image: cartoon 1- ordering prescription, cartoon 2- dispensing medication, cartoon 3- patient collecting prescritpion.
I also need to highlight our services which include
medicine use review
pharmacy first*
Morning after pill*
emergency supply service*
seasonal flu vaccinations*
on the other side i need a consent form for ETP nomination to include full name, address, date of birth, NHS number, signature and current date
this shoudl be on the top half of the leaftet.
On the bottom half or bottom quarter, I need writing:
Thornfield Pharmacy proudly uses a robotic dispensing system.

The Pharmacy directors have invested in this technology to enhance the service that we provide our customers.

Medication is dispensed from a high speed robotic arm within the unit which not only improves efficiency but also importantly maximises patient safety.

The robot in action can be witnessed through a viewing window positioned outside the shop window - it is truly remarkable to see. Please feel free to visit and view. Our staff will be only too happy to introduce you to our new addition and explain how the system works.

Target Market(s)

NHS patients ranging from 16 years to 80 years +

Industry/Entity Type

Pharmacy

Font styles to use
Serif

Requirements
Must have
• Name of pharmacy
• Address of pharmacy: Ashcombe Larkfield Centre, Kestrel Row, Ashcombe, Nottingham, NG4 2TW
• Telephone number:0115 9630587
• Opening times: Mon - Sat 7.30am - 10pm, sunday 8am - 9pm
• Services we offer: Prescription collection service
• minor ailments scheme
• emergency hormonal contraception
• Expert health advice
• Medicines disposal
• Prescription delivery service
• Our twitter handle: ourthornfield
• facebook page: ourthornfieldpharmacy
Nice to have
• colourful, upbeat vibe to the leaflet whilst including all the relevant information.
Should not have
• big pictures of people

```html
<!DOCTYPE html>
<html lang="en">
<head>
<meta charset="utf-8">
<title>Thornfield Pharmacy – Flyer</title>
<link rel="stylesheet" href="https://fonts.googleapis.com/css2?family=Archivo+Black&family=Lato:wght@700;900&family=Oswald:wght@300;400;600&display=swap">
<style>
  :root {
    --navy: #13205e;
    --navy-deep: #0d1a4f;
    --sky: #29a8e8;
    --sky-light: #7fd0f6;
    --white: #ffffff;
    --paper: #f1f3f5;
    --ink: #0f1c55;
  }
  * { box-sizing: border-box; margin: 0; padding: 0; }
  html, body { width: 900px; height: 1200px; overflow: hidden; background: var(--white); }
  .flyer { position: relative; width: 900px; height: 1200px; background: var(--paper); font-family: "Lato", sans-serif; color: var(--ink); overflow: hidden; }

  /* Header */
  .header { position: absolute; left: 0; top: 0; width: 900px; height: 250px; background: var(--white); }
  .brand { position: absolute; left: 55px; top: 52px; width: 240px; text-align: center; }
  .brand-mark { width: 70px; height: 70px; margin: 0 auto 14px; background: var(--navy); border-radius: 8px; }
  .brand-name { font-weight: 900; font-size: 28px; line-height: 1.15; color: var(--navy); }
  .title { position: absolute; right: 40px; top: 62px; text-align: center; }
  .title-main { font-family: "Archivo Black", sans-serif; font-size: 68px; line-height: 1; color: var(--navy); letter-spacing: 1px; }
  .title-sub { font-family: "Oswald", sans-serif; font-weight: 300; font-size: 74px; line-height: 1.05; color: var(--sky); letter-spacing: 3px; }

  /* Hero band */
  .hero { position: absolute; left: 0; top: 250px; width: 900px; height: 440px; background: var(--navy-deep); overflow: hidden; }
  .hero-visual { position: absolute; right: 0; top: 0; width: 560px; height: 440px;
    background: linear-gradient(90deg, var(--navy-deep) 0%, #1d3f86 35%, #5d8fc7 70%, #a9c9e6 100%); }
  .hero-text { position: absolute; left: 38px; top: 48px; width: 400px; color: var(--white); }
  .hero-lead { font-family: "Oswald", sans-serif; font-weight: 300; font-size: 52px; line-height: 1; letter-spacing: 1px; }
  .hero-mid { font-family: "Oswald", sans-serif; font-weight: 600; font-size: 31px; line-height: 1.2; letter-spacing: .5px; }
  .hero-strong { font-family: "Archivo Black", sans-serif; font-size: 52px; line-height: 1.1; letter-spacing: 1px; }
  .hero-rule { width: 360px; height: 3px; background: var(--white); margin: 26px 0 22px; }
  .contact-label { font-family: "Archivo Black", sans-serif; font-size: 46px; line-height: 1.1; }
  .contact-phone { font-family: "Oswald", sans-serif; font-weight: 400; font-size: 64px; line-height: 1.1; color: var(--sky-light); letter-spacing: 1px; }

  /* Product visual (behind text) */
  .product-visual { position: absolute; left: 0; top: 935px; width: 300px; height: 200px; z-index: 1;
    background: radial-gradient(ellipse at 35% 40%, #f5a623 0%, #f08a12 30%, #f3e8c8 58%, rgba(241,243,245,0) 72%); }

  /* Opening times */
  .hours { position: absolute; left: 25px; top: 720px; width: 480px; text-align: center; z-index: 2; }
  .hours-tab { display: block; margin: 0 auto 26px; width: 370px; height: 54px; border-radius: 12px;
    background: linear-gradient(180deg, var(--sky-light), var(--sky)); box-shadow: 0 3px 6px rgba(0,0,0,.2);
    font-weight: 900; font-size: 28px; line-height: 54px; color: var(--navy); }
  .hours-line { font-family: "Oswald", sans-serif; font-weight: 600; font-size: 40px; line-height: 1.2; color: var(--navy); white-space: nowrap; letter-spacing: -0.5px; }
  .hours-line.sunday { color: var(--sky); }

  /* Services */
  .services { position: absolute; left: 505px; top: 690px; width: 375px; height: 290px; background: var(--sky); z-index: 2;
    border-radius: 0 0 16px 16px; padding: 12px 20px 0 20px; color: var(--white); box-shadow: -4px 4px 10px rgba(0,0,0,.2); }
  .services-title { font-weight: 900; font-size: 27px; color: var(--navy); margin-bottom: 10px; }
  .services-list { list-style: none; }
  .services-list li { position: relative; padding-left: 22px; font-weight: 900; font-size: 20px; line-height: 1.0; margin-bottom: 11px; }
  .services-list li::before { content: ""; position: absolute; left: 2px; top: 7px; width: 7px; height: 7px; border-radius: 50%; background: var(--white); }

  /* Social bar */
  .social { position: absolute; left: 0; top: 1010px; width: 900px; height: 60px; background: var(--navy); z-index: 0;
    display: flex; align-items: center; justify-content: flex-end; gap: 20px; padding-right: 40px; color: var(--white); }
  .social-item { display: flex; align-items: center; gap: 14px; font-weight: 700; font-size: 23px; }
  .social-dot { width: 22px; height: 22px; background: var(--sky-light); border-radius: 3px; }

  /* Footer */
  .footer { position: absolute; left: 0; top: 1120px; width: 900px; height: 80px; background: var(--sky); z-index: 2;
    display: flex; align-items: center; padding-left: 45px; gap: 12px; font-weight: 700; font-size: 21px; color: var(--navy); }
  .footer svg { width: 26px; height: 24px; }
</style>
</head>
<body>
<div class="flyer">
  <header class="header">
    <div class="brand">
      <div class="brand-mark"></div>
      <div class="brand-name">Thornfield<br>Pharmacy</div>
    </div>
    <div class="title">
      <div class="title-main">THORNFIELD</div>
      <div class="title-sub">PHARMACY</div>
    </div>
  </header>

  <section class="hero">
    <div class="hero-visual" role="img" aria-label="Blue scientific image of a DNA helix and molecule structures"></div>
    <div class="hero-text">
      <div class="hero-lead">INDEPENDENT</div>
      <div class="hero-mid">HEALTH CENTRE BASED</div>
      <div class="hero-strong">PHARMACY</div>
      <div class="hero-rule"></div>
      <div class="contact-label">Contact Us</div>
      <div class="contact-phone">0115 9630587</div>
    </div>
  </section>

  <div class="social">
    <div class="social-item"><span class="social-dot"></span>ourthornfield</div>
    <div class="social-item"><span class="social-dot"></span>ourthornfieldpharmacy</div>
  </div>

  <div class="product-visual" role="img" aria-label="Orange pill bottle spilling white tablets"></div>

  <section class="hours">
    <span class="hours-tab">OPENING TIMES</span>
    <div class="hours-line">MON - SAT 7.30AM - 10PM</div>
    <div class="hours-line sunday">SUNDAY 8AM - 9PM</div>
  </section>

  <section class="services">
    <h2 class="services-title">Services</h2>
    <ul class="services-list">
      <li>emergency hormonal contraception</li>
      <li>Prescription collection service</li>
      <li>minor ailments scheme</li>
      <li>Expert health advice</li>
      <li>Medicines disposal</li>
      <li>Prescription delivery service</li>
    </ul>
  </section>

  <footer class="footer">
    <svg viewBox="0 0 26 24" aria-hidden="true"><path d="M13 1 L25 12 L21.5 12 L21.5 23 L15.5 23 L15.5 16 L10.5 16 L10.5 23 L4.5 23 L4.5 12 L1 12 Z" fill="#13205e"/></svg>
    <span>Ashcombe Larkfield Centre, Kestrel Row, Ashcombe, Nottingham, NG4 2TW</span>
  </footer>
</div>
</body>
</html>
```